Business Card Makeover. Recreate a sleek modern design for our business card.

DO NOT COPY OUR CURRENT DESIGN. MUST BE ONE SIDED BUSINESS CARD.
Create a new business card design, using our new logo. Attached is a sample of our current design and new logo. Please note the address and email will change. The new address is 417 Corvell West Palm Beach 33472 and our website will be www.talvendrake.example.

We are an architectural and interior design firm. We prefer a clean modern look. Something that is refined and emulates excellence.

Industry/Entity Type

Architecture

Contact Information for Business Card

clean modern look, please do not copy our attached design.

Font styles to use
Other font styles liked:
• see attached business card font

Colors

Designer to choose colors to be used in the design.

Requirements
Must have
• Must have a modern appeal and resemble our current branding.
Nice to have
• modern font, our logo, legible name and titles progressive design
Should not have
• Do not add colors not reflected in our branding. Should not look like our current card.

```html
<!DOCTYPE html>
<html lang="en">
<head>
<meta charset="utf-8">
<title>Talvendrake + Partners — Business Card</title>
<link rel="stylesheet" href="https://fonts.googleapis.com/css2?family=Raleway:wght@300;400;700&display=swap">
<style>
  :root {
    --backdrop: #e6e6e6;
    --card: #ffffff;
    --card-shade: #eef0f3;
    --accent: #2b7dc3;
    --ink: #3b3b3b;
    --muted: #6f6f6f;
    --edge: #1f1f1f;
    --deco: #e3e8ef;
  }
  html, body {
    margin: 0;
    width: 1200px;
    height: 1022px;
    overflow: hidden;
    background: var(--backdrop);
    font-family: "Raleway", Arial, sans-serif;
  }
  .card {
    position: absolute;
    left: 110px;
    top: 231px;
    width: 980px;
    height: 560px;
    background: linear-gradient(135deg, var(--card-shade) 0%, var(--card) 55%);
    box-shadow: 0 10px 30px rgba(0,0,0,0.18);
    overflow: hidden;
  }
  .card__edge {
    position: absolute;
    right: 0;
    top: 0;
    width: 14px;
    height: 100%;
    background: var(--edge);
  }
  .card__deco {
    position: absolute;
    left: 0;
    bottom: 0;
    width: 470px;
    height: 400px;
    background: radial-gradient(ellipse at 70% 10%, var(--deco) 0%, rgba(227,232,239,0.5) 45%, rgba(255,255,255,0) 75%);
  }
  .details {
    position: absolute;
    left: 520px;
    top: 44px;
    color: var(--ink);
    font-weight: 300;
  }
  .brand {
    display: flex;
    align-items: center;
    gap: 14px;
    margin-bottom: 22px;
  }
  .brand__mark {
    width: 46px;
    height: 46px;
    border-radius: 50%;
    background: var(--accent);
  }
  .brand__name {
    font-size: 32px;
    font-weight: 300;
    letter-spacing: 1px;
    color: var(--muted);
    line-height: 1;
  }
  .brand__name small {
    display: block;
    font-size: 11px;
    letter-spacing: 5px;
    margin-top: 6px;
    text-align: right;
  }
  .person__name {
    margin: 0;
    font-size: 26px;
    font-weight: 700;
    letter-spacing: 1px;
    color: var(--accent);
    line-height: 1.2;
  }
  .person__title {
    margin: 0 0 18px;
    font-size: 23px;
    color: var(--muted);
  }
  .address {
    font-style: normal;
    font-size: 23px;
    line-height: 1.25;
    margin-bottom: 16px;
  }
  .contacts {
    list-style: none;
    margin: 0 0 14px;
    padding: 0;
    font-size: 21px;
  }
  .contacts li {
    display: flex;
    align-items: center;
    gap: 12px;
    height: 31px;
  }
  .contacts svg {
    width: 18px;
    height: 18px;
    fill: var(--accent);
  }
  .practice {
    margin: 0;
    font-size: 21px;
    line-height: 1.3;
  }
  .license {
    margin: 0;
    font-size: 21px;
    color: var(--accent);
  }
</style>
</head>
<body>
  <div class="card">
    <div class="card__deco" role="img" aria-label="Faint brand decoration"></div>
    <div class="card__edge"></div>

    <div class="details">
      <div class="brand">
        <span class="brand__mark"></span>
        <span class="brand__name">TALVENDRAKE<small>+ PARTNERS</small></span>
      </div>

      <h1 class="person__name">MARCUS HELLER</h1>
      <p class="person__title">Partner / Director of Design</p>

      <address class="address">417 Corvell West<br>Palm Beach 33472</address>

      <ul class="contacts">
        <li>
          <svg viewBox="0 0 20 20" aria-label="Office phone"><path d="M5 2h3l1.5 4-2 1.3a11 11 0 0 0 5.2 5.2L14 10.5l4 1.5v3c0 1.1-.9 2-2 2A14 14 0 0 1 3 4c0-1.1.9-2 2-2z"/></svg>
          555.201.4410
        </li>
        <li>
          <svg viewBox="0 0 20 20" aria-label="Fax"><path d="M5 2h10v5H5zM2 8h16v7h-3v3H5v-3H2zm5 6v2h6v-2z"/></svg>
          555.201.4411
        </li>
        <li>
          <svg viewBox="0 0 20 20" aria-label="Mobile"><path d="M6 1h8a1 1 0 0 1 1 1v16a1 1 0 0 1-1 1H6a1 1 0 0 1-1-1V2a1 1 0 0 1 1-1zm1 2v12h6V3zm3 13a1 1 0 1 0 0 2 1 1 0 0 0 0-2z"/></svg>
          555.318.7702
        </li>
        <li>
          <svg viewBox="0 0 20 20" aria-label="Email"><path d="M2 4h16v12H2zm1.5 1.5v.4L10 11l6.5-5.1v-.4zm0 2.3v6.7h13V7.8L10 13z"/></svg>
          marcus@talvendrake.example
        </li>
        <li>
          <svg viewBox="0 0 20 20" aria-label="Website"><path d="M10 1a9 9 0 1 0 0 18 9 9 0 0 0 0-18zm0 2c.9 0 2 1.9 2.4 5H7.6C8 4.9 9.1 3 10 3zM3.1 8H5.6c.1-1.8.5-3.3 1-4.4A7 7 0 0 0 3.1 8zm0 4a7 7 0 0 0 3.5 4.4c-.5-1.1-.9-2.6-1-4.4zm4.5 0c.4 3.1 1.5 5 2.4 5s2-1.9 2.4-5zm6.8 0c-.1 1.8-.5 3.3-1 4.4a7 7 0 0 0 3.5-4.4zm2.5-4a7 7 0 0 0-3.5-4.4c.5 1.1.9 2.6 1 4.4zM7.5 10c0-.3 0-.7.1-1h4.8l.1 1-.1 1H7.6z"/></svg>
          www.talvendrake.example
        </li>
      </ul>

      <p class="practice">Architecture + Interior Design</p>
      <p class="license">LIC.# AA10457321</p>
    </div>
  </div>
</body>
</html>
```